Youth deer hunt give away flyer.

We need a flyer designed for a youth deer hunt giveaway that we are doing. We are an Illinois whitetail deer hunting outfitter. We house and feed our clients as well as providing them with a guided deer hunt. It needs to include images as well as details about the giveaway. Im looking for a proffesional, looking flyer

Target Market(s)

rednecks, hunters

Industry/Entity Type

Hunting

Font styles to use
Serif
Sans Serif

Colors
000000
dbdbdb
ffffff
474747

Requirements
Must have
• not sure
Nice to have
• not sure
Should not have
• not sure

```html
<!DOCTYPE html>
<html lang="en">
<head>
<meta charset="utf-8">
<title>2018 Youth Firearm Hunt Flyer</title>
<link rel="stylesheet" href="https://fonts.googleapis.com/css2?family=Cinzel:wght@400;600&family=Jost:wght@400;500&display=swap">
<style>
  :root {
    --black: #000000;
    --ink: #141414;
    --charcoal: #474747;
    --silver: #dbdbdb;
    --white: #ffffff;
    --text-dark: #1e1e1e;
  }
  * { margin: 0; padding: 0; box-sizing: border-box; }
  html, body { width: 1200px; height: 1200px; overflow: hidden; }
  body { background: #ececec; position: relative; font-family: "Jost", sans-serif; }

  .flyer {
    position: absolute; left: 190px; top: 30px;
    width: 820px; height: 1140px;
    background: radial-gradient(ellipse at 70% 40%, #2a2a2a 0%, var(--ink) 60%, var(--black) 100%);
    overflow: hidden;
  }
  .hero-art { position: absolute; left: 0; top: 0; width: 820px; height: 660px; }

  .cabin-photo {
    position: absolute; left: 62px; top: 413px;
    width: 190px; height: 190px; border-radius: 50%;
    border: 7px solid var(--white);
    background: linear-gradient(180deg, #e9e6da 0%, #c9a45a 40%, #7a5a35 62%, #6f9a3c 78%, #4f7d2a 100%);
    box-shadow: 0 3px 8px rgba(0,0,0,.45);
  }

  .brand {
    position: absolute; left: 500px; top: 360px; width: 260px;
    text-align: center; color: var(--white);
  }
  .brand-mark {
    width: 92px; height: 92px; margin: 0 auto 22px;
    border-radius: 50%; border: 3px solid var(--silver);
  }
  .brand-name { font-family: "Cinzel", serif; font-size: 29px; letter-spacing: 1px; line-height: 1; }
  .brand-sub { font-family: "Cinzel", serif; font-size: 12px; letter-spacing: 4px; margin-top: 8px; color: var(--silver); }

  .event-title {
    position: absolute; left: 0; top: 615px; width: 820px;
    text-align: center; font-family: "Cinzel", serif; font-weight: 400;
    font-size: 40px; color: var(--white); letter-spacing: .5px;
  }

  .details {
    position: absolute; left: 0; top: 668px; width: 820px; height: 256px;
    background: linear-gradient(180deg, #f4f4f4 0%, var(--silver) 55%, #cfcfcf 100%);
    border-top: 6px solid #9a9a9a;
    border-bottom: 6px solid #9a9a9a;
    text-align: center; color: var(--text-dark);
    padding-top: 14px;
  }
  .details p { font-size: 21px; text-transform: uppercase; line-height: 1.2; padding: 6px 0; }
  .details .rule { width: 560px; height: 1px; background: var(--text-dark); margin: 2px auto; }
  .details .rule.short { width: 200px; }
  .details .rule.mid { width: 260px; }

  .footer {
    position: absolute; left: 0; top: 930px; width: 820px; height: 210px;
    display: flex; padding: 22px 26px; color: var(--white);
  }
  .about { width: 300px; padding-right: 18px; border-right: 1px solid var(--silver); }
  .about h3 { font-family: "Cinzel", serif; font-weight: 400; font-size: 14px; margin-bottom: 4px; }
  .about p { font-size: 9.6px; line-height: 1.32; text-align: justify; color: #e6e6e6; }

  .contact { width: 210px; padding: 4px 18px; border-right: 1px solid var(--silver); }
  .contact h3 {
    font-family: "Cinzel", serif; font-weight: 400; font-size: 19px;
    padding-bottom: 4px; border-bottom: 1px solid var(--silver); display: inline-block; margin-bottom: 16px;
  }
  .contact-row { display: flex; gap: 10px; font-size: 12.5px; line-height: 1.35; margin-bottom: 14px; }
  .contact-row svg { flex: none; margin-top: 3px; }

  .online { flex: 1; padding: 4px 0 0 20px; }
  .online .contact-row { font-size: 11.5px; margin-bottom: 10px; }
  .social { display: flex; gap: 20px; margin: 14px 0 0 38px; }
  .social span { width: 36px; height: 36px; background: var(--silver); display: block; }
</style>
</head>
<body>
  <main class="flyer">
    <svg class="hero-art" viewBox="0 0 820 660" aria-hidden="false">
      <defs>
        <linearGradient id="fieldTone" x1="0" y1="0" x2="0" y2="1">
          <stop offset="0" stop-color="#d9d6cf"/>
          <stop offset=".35" stop-color="#8f7c5a"/>
          <stop offset=".7" stop-color="#6e5a3a"/>
          <stop offset="1" stop-color="#4e4a2c"/>
        </linearGradient>
        <linearGradient id="swoosh" x1="0" y1="0" x2="1" y2="1">
          <stop offset="0" stop-color="#ffffff"/>
          <stop offset=".5" stop-color="#9a9a9a"/>
          <stop offset="1" stop-color="#e6e6e6"/>
        </linearGradient>
      </defs>
      <path d="M0 0 H745 C725 260 500 585 250 595 C150 598 60 525 0 465 Z" fill="url(#swoosh)"/>
      <path role="img" aria-label="Photo of a smiling hunter in camouflage posing with a large whitetail buck in a grassy field"
            d="M0 0 H722 C700 250 480 562 250 573 C150 578 60 500 0 442 Z" fill="url(#fieldTone)"/>
    </svg>

    <div class="cabin-photo" role="img" aria-label="Photo of the private log cabin lodging on a green lawn"></div>

    <div class="brand">
      <div class="brand-mark"></div>
      <div class="brand-name">HARLAN RIDGE</div>
      <div class="brand-sub">OUTFITTING</div>
    </div>

    <h1 class="event-title">2018 YOUTH FIREARM HUNT</h1>

    <section class="details">
      <p>October 6-8, 2018</p>
      <div class="rule short"></div>
      <p>4 night stay in our private cabin that include<br>meals for 2 parents and the child.</p>
      <div class="rule"></div>
      <p>Guided shotgun hunt on strictly managed properties.</p>
      <div class="rule mid"></div>
      <p>Ground blinds in place</p>
      <div class="rule mid"></div>
      <p>Permit &amp; license fees are the hunters responsibility.</p>
    </section>

    <footer class="footer">
      <div class="about">
        <h3>About Us</h3>
        <p>Harlan Ridge Outfitting is a family owned and operated deer hunting outfitter located in Morgan and Scott Counties in west central Illinois. We provide low pressure, trophy whitetail hunts on privately owned farms across the region. The Harlans are lifelong residents and hunters of Morgan County, with the family farm being established well over 150 years ago. To go along with guiding deer and turkey hunters, we also offer a wide variety of professional hunting services that include whitetail land consulting, scouting services, CRP and food plot plantings and more.</p>
      </div>

      <div class="contact">
        <h3>Dale Harlan</h3>
        <div class="contact-row">
          <svg width="10" height="13" viewBox="0 0 10 13"><path d="M5 0a5 5 0 0 0-5 5c0 3.5 5 8 5 8s5-4.5 5-8a5 5 0 0 0-5-5zm0 7a2 2 0 1 1 0-4 2 2 0 0 1 0 4z" fill="#dbdbdb"/></svg>
          <span>1847 Ridge Road<br>Millbrook, Illinois 62000</span>
        </div>
        <div class="contact-row">
          <svg width="11" height="11" viewBox="0 0 11 11"><path d="M2.2 0.5l1.8 2.3-1 1.2c.7 1.6 2 2.9 3.6 3.6l1.2-1 2.3 1.8-.9 1.9C5 10.3.7 6 .3 1.4z" fill="#dbdbdb"/></svg>
          <span>(555) 014-2297</span>
        </div>
      </div>

      <div class="online">
        <div class="contact-row">
          <svg width="10" height="10" viewBox="0 0 10 10"><circle cx="5" cy="5" r="4" fill="none" stroke="#dbdbdb" stroke-width="1.6"/><circle cx="5" cy="5" r="1.5" fill="#dbdbdb"/></svg>
          <span>harlanridgeoutfitting@mail.example</span>
        </div>
        <div class="contact-row">
          <svg width="10" height="10" viewBox="0 0 10 10"><circle cx="5" cy="5" r="4.5" fill="#dbdbdb"/></svg>
          <span>www.harlanridgeoutfitting.example</span>
        </div>
        <div class="social" aria-label="Social media links">
          <span></span><span></span>
        </div>
      </div>
    </footer>
  </main>
</body>
</html>
```